Outdoor sign for Brightwater Auto Restoration

I need a horizontal 4'x 8' outdoor roadside sign for my classic auto restoration business. I have uploaded colors and our logo. Needs the Brightwater name, a prominent Classic AUTO RESTORATION, phone number and website. We rebuild and restore vintage cars, trucks and 4x4s. I'd like something clean but possibly retro. Classic Auto Restoration is more important than the Brightwater name. It needs to be visible and readable from the street. NO CLIP ART

Target Market(s)

Customers who need their vintage care restored or upgraded. Men and women ages 25-75

Industry/Entity Type

Automotive

Colors
FFC000
F8CF3A
FAE287
FDF2CF
FEFAEE

Requirements
Must have
• Legible. Bright. Readable as a backlit 4' x 8' large horizontal sign (roughly 120cm X 240cm)
Nice to have
• Use of the Brightwater logo/type, Complete or Classic before prominent AUTO RESTORATION
Should not have
• Clip art of old cars or icons. And we don't want the Brightwater Logo from the website because it wont be legible from the road. I have included the Illustrator file for Brightwater text in the uploads

```html
<!DOCTYPE html>
<html lang="en">
<head>
<meta charset="utf-8">
<title>Brightwater Auto Restoration – Roadside Sign</title>
<link rel="stylesheet" href="https://fonts.googleapis.com/css2?family=Orbitron:wght@900&family=Oswald:wght@700&family=Rubik:wght@400;500&family=Open+Sans:wght@800&display=swap">
<style>
  :root {
    --canvas: #000000;
    --sign-yellow: #fdf002;
    --sign-pale: #f8e48a;
    --sign-orange: #fdc010;
    --ink: #000000;
    --paper: #ffffff;
  }
  html, body {
    margin: 0;
    padding: 0;
    width: 1200px;
    height: 927px;
    overflow: hidden;
    background: var(--canvas);
  }
  .sign {
    display: block;
    width: 1200px;
    height: 927px;
  }
  .panel-yellow { fill: var(--sign-yellow); stroke: var(--paper); stroke-width: 1; }
  .panel-pale { fill: var(--sign-pale); }
  .panel-orange { fill: var(--sign-orange); }
  .stitch { fill: none; stroke: var(--paper); stroke-width: 1.2; stroke-dasharray: 3 3; }
  .phone-band { fill: var(--ink); }
  .brand-name {
    font-family: "Oswald", "Arial Narrow", sans-serif;
    font-weight: 700;
    fill: var(--paper);
  }
  .headline {
    font-family: "Orbitron", "Arial Black", sans-serif;
    font-weight: 900;
    fill: var(--ink);
  }
  .tagline {
    font-family: "Rubik", "Helvetica", sans-serif;
    font-weight: 400;
    font-size: 45px;
    fill: var(--ink);
  }
  .phone-number {
    font-family: "Open Sans", "Arial", sans-serif;
    font-weight: 800;
    fill: var(--paper);
  }
  .website {
    font-family: "Rubik", "Helvetica", sans-serif;
    font-weight: 500;
    fill: var(--ink);
  }
  .icon-line { fill: none; stroke: var(--ink); stroke-width: 3; }
</style>
</head>
<body>
<svg class="sign" viewBox="0 0 1200 927" xmlns="http://www.w3.org/2000/svg" role="img" aria-label="Brightwater Classic Auto Restoration roadside sign">
  <!-- backgrounds -->
  <rect class="panel-yellow" x="36" y="180" width="1132" height="566"/>
  <path class="panel-pale" d="M651 180 H1168 V651 H621 C740 590 805 490 805 396 C805 340 795 310 780 286 C720 250 680 215 651 180 Z"/>
  <path class="panel-orange" d="M651 180 H1168 V263 C1080 305 1010 319 956 319 C870 319 800 295 755 268 C710 242 675 212 651 180 Z"/>
  <path class="stitch" d="M651 183 C675 213 710 244 755 272 C800 298 870 331 956 331 C1020 331 1090 312 1166 268"/>
  <path class="stitch" d="M785 296 C800 320 817 350 817 396 C817 495 750 595 625 654"/>

  <!-- bottom band -->
  <path class="phone-band" d="M36 651 H615 L581 746 H36 Z"/>
  <path class="panel-pale" d="M615 651 H630 L598 746 H581 Z"/>

  <!-- brand -->
  <text class="brand-name" x="958" y="266" font-size="62" text-anchor="middle" textLength="330" lengthAdjust="spacingAndGlyphs">BRIGHTWATER</text>

  <!-- headline -->
  <text class="headline" x="168" y="328" font-size="72" textLength="483" lengthAdjust="spacingAndGlyphs">CLASSIC</text>
  <text class="headline" x="51" y="481" font-size="168" textLength="717" lengthAdjust="spacingAndGlyphs">AUTO</text>
  <text class="headline" x="108" y="560" font-size="64" textLength="602" lengthAdjust="spacingAndGlyphs">RESTORATION</text>

  <!-- services -->
  <text class="tagline" text-anchor="middle">
    <tspan x="981" y="390">We</tspan>
    <tspan x="981" y="438">Rebuild And</tspan>
    <tspan x="981" y="486">Restore</tspan>
    <tspan x="981" y="533">VINTAGE CARS,</tspan>
    <tspan x="981" y="581">TRUCKS and</tspan>
    <tspan x="981" y="628">4X4S</tspan>
  </text>

  <!-- phone -->
  <g class="phone-icon" fill="var(--paper)">
    <path d="M70 682 C64 686 62 694 66 703 C73 716 84 726 96 731 C103 734 108 731 111 727 L104 718 C101 716 98 717 95 720 C88 717 81 710 77 702 C80 699 81 696 79 693 Z"/>
    <path d="M88 686 A14 14 0 0 1 100 698" fill="none" stroke="var(--paper)" stroke-width="3"/>
    <path d="M89 677 A22 22 0 0 1 109 697" fill="none" stroke="var(--paper)" stroke-width="3"/>
  </g>
  <text class="phone-number" x="114" y="728" font-size="82" textLength="455" lengthAdjust="spacingAndGlyphs">501-555-0142</text>

  <!-- website -->
  <g class="globe-icon">
    <circle class="icon-line" cx="649" cy="703" r="18"/>
    <ellipse class="icon-line" cx="649" cy="703" rx="8" ry="18"/>
    <line class="icon-line" x1="631" y1="703" x2="667" y2="703"/>
    <line class="icon-line" x1="634" y1="694" x2="664" y2="694"/>
    <line class="icon-line" x1="634" y1="712" x2="664" y2="712"/>
  </g>
  <text class="website" x="680" y="716" font-size="42" textLength="471" lengthAdjust="spacingAndGlyphs">brightwaterautoworks.com</text>
</svg>
</body>
</html>
```